Stationery Design
Business Card, Envelopes and letterhead
Professional
Dwight Halloway
Production Manager
4172 N. Wrenfield Rd.
Baton Rouge LA 70913
dwight@velmorpack.com
www.velmorpack.com
Please propose letterhead, business card and envelope design using the new logo just uploaded

```html
<!DOCTYPE html>
<html lang="en">
<head>
<meta charset="utf-8">
<title>VPK Stationery Set</title>
<link rel="stylesheet" href="https://fonts.googleapis.com/css2?family=Arimo:wght@400;700&display=swap">
<style>
  :root {
    --bg-light: #8a8a8a;
    --bg-dark: #4a4a4a;
    --paper: #ffffff;
    --brand-blue: #1aa3e0;
    --ink: #2b2b2b;
    --table-grey: #c9c9c9;
    --window-grey: #d6d6d6;
    --window-edge: #9a9a9a;
    --hub-grey: #888888;
  }
  html, body {
    margin: 0;
    padding: 0;
    overflow: hidden;
  }
  .stage {
    width: 1200px;
    height: 605px;
    background: radial-gradient(ellipse at center, var(--bg-light) 0%, var(--bg-dark) 100%);
    overflow: hidden;
  }
  .stage svg {
    display: block;
    font-family: "Arimo", sans-serif;
  }
  .brand-name { fill: var(--brand-blue); font-weight: 700; }
  .brand-sub { fill: var(--brand-blue); font-weight: 700; }
  .text-ink { fill: var(--ink); }
  .text-white { fill: var(--paper); }
  .paper { fill: var(--paper); }
  .band { fill: var(--brand-blue); }
  .rule { stroke: var(--brand-blue); stroke-width: 2; }
  .table-head { fill: var(--table-grey); }
  .table-line { stroke: var(--table-grey); stroke-width: 1; fill: none; }
  .address-window { fill: var(--window-grey); stroke: var(--window-edge); }
  .disc-hub { fill: var(--hub-grey); }
</style>
</head>
<body>
<main class="stage">
<svg width="1200" height="605" viewBox="0 0 1200 605" xmlns="http://www.w3.org/2000/svg">

  <defs>
    <linearGradient id="discTone" x1="0" y1="0" x2="1" y2="1">
      <stop offset="0" stop-color="#111111"/>
      <stop offset="0.45" stop-color="#555555"/>
      <stop offset="0.6" stop-color="#f2f2f2"/>
      <stop offset="1" stop-color="#ffffff"/>
    </linearGradient>
  </defs>

  <!-- Business card, front -->
  <g class="business-card-front">
    <rect class="paper" x="24" y="5" width="240" height="140"/>
    <text class="text-ink" x="92" y="20" font-size="10">Dwight Halloway</text>
    <text class="text-ink" x="92" y="30" font-size="6">Production Manager</text>
    <text class="brand-name" x="80" y="78" font-size="28">VPK</text>
    <text class="brand-sub" x="80" y="89" font-size="6">VELMOR PACKAGING</text>
    <path class="band" d="M24 108 Q144 88 264 112 L264 145 L24 145 Z"/>
    <text class="text-white" x="34" y="124" font-size="6">4172 N. Wrenfield Rd.</text>
    <text class="text-white" x="34" y="133" font-size="6">Baton Rouge LA 70913</text>
    <text class="text-white" x="160" y="124" font-size="6">dwight@velmorpack.com</text>
    <text class="text-white" x="160" y="133" font-size="6">www.velmorpack.com</text>
  </g>

  <!-- Business card, back -->
  <g class="business-card-back">
    <rect class="paper" x="62" y="172" width="196" height="128" rx="64"/>
    <path class="band" d="M100 172 L222 172 Q250 178 258 200 Q160 182 66 210 Q74 182 100 172 Z"/>
    <text class="text-ink" x="150" y="222" font-size="9">Dwight Halloway</text>
    <text class="text-ink" x="150" y="231" font-size="5.5">Production Manager</text>
    <text class="brand-name" x="106" y="262" font-size="24">VPK</text>
    <text class="brand-sub" x="106" y="271" font-size="5.5">VELMOR PACKAGING</text>
    <text class="text-ink" x="96" y="283" font-size="5.5">4172 N. Wrenfield Rd.</text>
    <text class="text-ink" x="96" y="291" font-size="5.5">Baton Rouge LA 70913</text>
  </g>

  <!-- Envelope -->
  <g class="envelope">
    <rect class="paper" x="10" y="317" width="326" height="247"/>
    <path class="band" d="M10 317 L336 317 L336 345 Q173 305 10 350 Z"/>
    <text class="brand-name" x="262" y="398" font-size="22">VPK</text>
    <text class="brand-sub" x="262" y="407" font-size="5.5">VELMOR PACKAGING</text>
    <rect class="address-window" x="156" y="451" width="96" height="38"/>
    <text class="text-ink" x="28" y="500" font-size="6">4172 N. Wrenfield Rd.</text>
    <text class="text-ink" x="28" y="509" font-size="6">Baton Rouge LA 70913</text>
    <path class="band" d="M10 530 Q173 520 336 545 L336 564 L10 564 Z"/>
  </g>

  <!-- Letterhead -->
  <g class="letterhead">
    <rect class="paper" x="343" y="19" width="389" height="562"/>
    <text class="brand-name" x="362" y="52" font-size="26">VPK</text>
    <text class="brand-sub" x="362" y="62" font-size="5.5">VELMOR PACKAGING</text>
    <line class="rule" x1="356" y1="68" x2="718" y2="68"/>
    <path class="band" d="M343 520 Q540 485 732 530 L732 581 L343 581 Z"/>
    <text class="text-white" x="360" y="565" font-size="6.5">4172 N. Wrenfield Rd. · Baton Rouge LA 70913</text>
  </g>

  <!-- Invoice -->
  <g class="invoice">
    <rect class="paper" x="763" y="19" width="413" height="562"/>
    <text class="brand-name" x="780" y="48" font-size="24">VPK</text>
    <text class="brand-sub" x="780" y="58" font-size="5.5">VELMOR PACKAGING</text>
    <text class="text-ink" x="1072" y="68" font-size="8" font-weight="700">INVOICE</text>
    <text class="text-ink" x="1072" y="80" font-size="8">Date :</text>
    <text class="text-ink" x="782" y="110" font-size="8">BILL TO:</text>
    <line class="table-line" x1="782" y1="135" x2="1160" y2="135"/>
    <rect class="table-head" x="782" y="142" width="378" height="13"/>
    <text class="text-ink" x="785" y="152" font-size="8">DESCRIPTION</text>
    <text class="text-ink" x="1064" y="152" font-size="8">AMOUNT</text>
    <line class="table-line" x1="1060" y1="142" x2="1060" y2="370"/>
    <rect class="table-line" x="782" y="142" width="378" height="228"/>
    <rect class="table-head" x="1060" y="355" width="100" height="15"/>
    <text class="text-ink" x="1064" y="366" font-size="8">TOTAL</text>
    <path class="band" d="M763 520 Q970 485 1176 530 L1176 581 L763 581 Z"/>
    <text class="text-white" x="780" y="565" font-size="6.5">4172 N. Wrenfield Rd. · Baton Rouge LA 70913</text>
  </g>

  <!-- Disc -->
  <g class="disc">
    <circle cx="696" cy="324" r="139" fill="var(--paper)"/>
    <circle cx="696" cy="324" r="137" role="img" aria-label="Disc label artwork with sweeping black and white curves" fill="url(#discTone)"/>
    <circle cx="696" cy="324" r="30" fill="#333333"/>
    <circle class="disc-hub" cx="696" cy="324" r="22"/>
    <circle cx="696" cy="324" r="7" fill="var(--bg-light)"/>
    <text class="brand-name" x="758" y="408" font-size="22">VPK</text>
    <text class="brand-sub" x="758" y="418" font-size="5.5">VELMOR PACKAGING</text>
  </g>
</svg>
</main>
</body>
</html>
```